Villa Serena needs a new website for its boutique apartment

We are a boutique apartment in Florence that rents out to tourists. We are looking to redesign our website. See the existing site at www.villaserena-stay.example

Ideally redesigned site would enable us to easily add and change photos in the gallery and across the site.

The new logo for the apartment is currently under design but being based around the current house logo with a person standing inside.
Updates

Reason: The website design by the 1st Place designer has been long and drawn out and not led to the design that we were looking for. As such, we are extending the deadline for another 5 days to hopefully get new designs and options.

Target Market(s)

Global tourists

Industry/Entity Type

Accommodation

Coding

Coded - Design and coding required

Number of Pages Required

5+ page

Font styles to use
Sans Serif

Requirements
Must have
• Welcome page, gallery page, information page about apartment and availability page with link to booking sites. And option for another page with tourist information. We must be able to change the photos in the gallery with relative ease when required.
• The Villa Serena font has been uploaded which is used with the logo and the new logo has been uploaded.
Nice to have
• Looking like a fun but professional hotel site
• Page info is located on www.villaserena-stay.example site

```html
<!DOCTYPE html>
<html lang="en">
<head>
<meta charset="utf-8">
<title>Villa Serena – Boutique Apartment in Florence</title>
<link href="https://fonts.googleapis.com/css2?family=Raleway:wght@300;400;500&family=Arimo:wght@400&display=swap" rel="stylesheet">
<style>
:root{
  --white:#ffffff;
  --stone:#d6d1c6;
  --stone-light:#e4e0d6;
  --band-outer:#6e6e6e;
  --band-inner:#404040;
  --cream:#fdfcf5;
  --footer:#3e3e3e;
  --accent:#e3653f;
  --accent-dark:#c9472a;
  --ink:#3a3a3a;
  --text-grey:#6a6a6a;
}
*{margin:0;padding:0;box-sizing:border-box}
html,body{width:1200px;height:915px;overflow:hidden}
body{position:relative;background:var(--cream);font-family:'Raleway',sans-serif;color:var(--ink)}
.site-header-band{position:absolute;left:0;top:0;width:1200px;height:110px;background:var(--white)}
.stone-band{position:absolute;left:0;top:110px;width:1200px;height:311px;background:linear-gradient(180deg,var(--stone-light),var(--stone) 65%,#c9c1b2)}
.header{position:absolute;left:200px;top:0;width:800px;height:92px;background:var(--white)}
.brand{position:absolute;left:19px;top:38px;height:24px;display:flex;align-items:center;gap:8px;font-weight:400;font-size:17px;color:#1e1e1e;letter-spacing:0.3px}
.brand-mark{width:12px;height:12px;background:#1e1e1e}
.nav{position:absolute;top:36px;left:0;width:800px;height:28px}
.nav a{position:absolute;top:0;height:28px;line-height:28px;font-size:15px;color:#2b2b2b;text-decoration:none;font-weight:400}
.nav a.active{background:#3f3f3f;color:var(--white);padding:0 16px}
.hero{position:absolute;left:200px;top:92px;width:800px;height:329px;background:linear-gradient(165deg,#d6c3a8 0%,#ece3d4 28%,#f7f3ec 50%,#e9ddcc 70%,#c49a86 88%,#9c6a5e 100%)}
.info-band{position:absolute;left:0;top:421px;width:1200px;height:111px;background:var(--band-outer)}
.info-inner{position:absolute;left:200px;top:0;width:800px;height:111px;background:var(--band-inner)}
.info-col{position:absolute;top:18px}
.info-col h2{font-weight:400;font-size:17px;color:var(--accent);line-height:19px}
.info-col p{font-family:'Arimo',sans-serif;font-size:10.4px;line-height:12.4px;color:#f0f0f0}
.col-space{left:29px;width:335px}
.col-guest{left:433px;width:345px}
.sketch{position:absolute;left:200px;top:580px;width:397px;height:228px;background:radial-gradient(ellipse 60% 55% at 55% 55%,#9a968e 0%,#c9c5bb 45%,#ece9e0 75%,var(--cream) 100%)}
.welcome{position:absolute;left:618px;top:592px;width:380px}
.welcome h1{font-weight:400;font-size:25px;line-height:28px;color:#444}
.rule{position:relative;margin-top:9px;width:239px;height:4px;background:var(--accent)}
.rule::before{content:"";position:absolute;left:0;top:0;width:55px;height:4px;background:var(--accent-dark)}
.welcome h3{margin-top:23px;font-weight:400;font-size:14.5px;color:var(--accent)}
.welcome p{margin-top:6px;font-size:10.4px;line-height:12.4px;color:var(--text-grey)}
.btn{position:absolute;left:618px;top:757px;width:94px;height:31px;background:var(--accent);color:var(--white);font-size:9.8px;line-height:31px;text-align:center;text-decoration:none}
.footer{position:absolute;left:0;top:869px;width:1200px;height:46px;background:var(--footer)}
.footer small{position:absolute;left:200px;top:17px;font-size:10px;color:#e8e8e8}
.social{position:absolute;left:936px;top:18px;display:flex;gap:8px}
.social span{width:10px;height:10px;border-radius:50%;background:var(--white)}
</style>
</head>
<body>
<div class="site-header-band"></div>
<div class="stone-band"></div>

<header class="header">
  <div class="brand"><span class="brand-mark"></span>VILLA SERENA</div>
  <nav class="nav">
    <a class="active" href="#" style="left:383px">Home</a>
    <a href="#" style="left:473px">About</a>
    <a href="#" style="left:546px">Gallery</a>
    <a href="#" style="left:626px">Contact</a>
    <a href="#" style="left:710px">Availablity</a>
  </nav>
</header>

<div class="hero" role="img" aria-label="Bright living room of the apartment with a beige sofa, tall windows, tulips and a red bean bag"></div>

<section class="info-band">
  <div class="info-inner">
    <div class="info-col col-space">
      <h2>THE SPACE</h2>
      <p>A newly renovated boutique 2-bedroom loft apartment in the historic centre of Florence, offering luxury accommodation for up to six adults. "Villa Serena" is a dedicated apartment for guests and is professionally cleaned and maintained to a high standard.</p>
    </div>
    <div class="info-col col-guest">
      <h2>OUR GUEST</h2>
      <p>Guests are provided complimentary bottles of water, Ortensia Firenze toiletries, coffee, tea and milk, and, full sized bath robes and slippers.</p>
    </div>
  </div>
</section>

<div class="sketch" role="img" aria-label="Ink sketch of the Florence skyline with the cathedral dome and bell tower"></div>

<section class="welcome">
  <h1>Welcome to Villa Serena</h1>
  <div class="rule"></div>
  <h3>Perfect location for sight sightseeing</h3>
  <p>&nbsp;"Villa Serena" is perfectly located for your Tuscan holiday, offering easy walking access to all of central Florence - only 600m from the Duomo and Ponte Vecchio.&nbsp;&nbsp; The apartment is configured to sleep up to six and is furnished with elegant and luxury fittings, and has complimentary high-speed internet and cable-TV.</p>
</section>
<a class="btn" href="#">LEARN MORE</a>

<footer class="footer">
  <small>© 2016 Villa Serena. All Rights Reserved</small>
  <div class="social"><span></span><span></span><span></span><span></span></div>
</footer>
</body>
</html>
```